Flyer-Design für verschiedene Anwendungsfälle bzw. Produkte
Zielgruppe
Wir lösen reale Probleme mit digitalen Technologien wie IoT und KI. In unseren Projekten liefern wir Gesamtlösungen von der Strategieberatung über Konzepterstellung bis zur technischen Umsetzung und dem Betrieb. Integration und Konzeption spielen eine große Rolle, wir sind kein Hardwareanbieter, sondern bauen Komplettlösungen aus Software, Connectivity und Hardware. Unsere Kunden sind gehobener Mittelstand bis Konzern, ab 25 Mio € aufwärts. Oft sind unsere Kunden aus konservativen Branchen. Wir müssen beim Design immer einen Kompromiss aus innovativ und Vertrauen erweckend finden. Unsere Persona ist weiß, männlich, über 50, nicht besonders technologieaffin.
Aufgabenstellung
Wir brauchen eine Flyer-Vorlage für verschiedene Anwendungsfälle bzw. Produkte. Im Anhang sind Beispiele für Produktbeschreibungen, sowie ein Flyer, den wir selbst designet haben.
Ergebnis soll ein Flyer-Design sein, das wir für solche Produkte immer wieder verwenden können, DIN A5 zweiseitig.
Exo2 und Trebuchet sind unsere Schriftarten. Logos habe ich in 2 Formaten angehängt.
Website: tavolu.me
Wenn Sie weitere Ideen haben, sind wir ganz Ohr.
Grafisch bitte nur die Farben grau, schwarz und orange verwenden (grau und orange siehe Logo)

```html
<!DOCTYPE html>
<html lang="de">
<head>
<meta charset="utf-8">
<title>Smart City Flyer – Grundwasserpegel-Messung per Funk</title>
<link href="https://fonts.googleapis.com/css2?family=Exo+2:wght@300;400;500;600;700;800&display=swap" rel="stylesheet">
<style>
  :root{
    --orange:#e0601b;
    --orange-dark:#d4491a;
    --orange-light:#e9a733;
    --grey-bg:#ececec;
    --grey-mid:#d6d6d6;
    --grey-line:#c9c9c9;
    --text:#2e2e2e;
    --white:#ffffff;
    --stage:#3a3a3e;
    --orange-grad:linear-gradient(90deg,var(--orange-dark) 0%,var(--orange) 40%,var(--orange-light) 100%);
  }
  *{box-sizing:border-box;margin:0;padding:0}
  html,body{width:1200px;height:800px;overflow:hidden}
  body{background:var(--stage);font-family:"Exo 2",sans-serif;color:var(--text);position:relative}

  .flyer-page{position:absolute;top:104px;width:424px;height:598px;background:var(--grey-bg);overflow:hidden;box-shadow:0 6px 18px rgba(0,0,0,.35)}
  .flyer-front{left:139px}
  .flyer-back{left:634px}
  .abs{position:absolute}

  /* ---------- front ---------- */
  .front-top{left:0;top:0;width:424px;height:280px;background:linear-gradient(180deg,#dcdcdc,#e9e9e9)}
  .brand{left:26px;top:38px;display:flex;align-items:center;gap:6px}
  .brand-name{font-weight:600;font-size:24px;letter-spacing:6px;color:var(--orange)}
  .brand-dot{width:9px;height:9px;border-radius:50%;background:var(--orange)}
  .city-photo{left:148px;top:71px;width:276px;height:209px;
    clip-path:polygon(0 0,100% 0,100% 100%,53% 100%);
    background:radial-gradient(circle at 60% 55%,#a0783c 0%,#4a3a4a 35%,#242236 75%,#1a1a28 100%)}
  .corner-shape{left:322px;top:33px;width:102px;height:67px;
    clip-path:polygon(0 0,100% 0,100% 100%,13% 100%);background:linear-gradient(90deg,var(--orange-light),var(--orange-dark))}
  .corner-shape-light{left:280px;top:33px;width:60px;height:40px;
    clip-path:polygon(70% 0,100% 0,100% 100%,0 100%);background:var(--orange-light);opacity:.85}
  .hero-band{left:0;top:110px;width:246px;height:132px;
    clip-path:polygon(0 0,70% 0,100% 100%,0 100%);background:var(--orange-grad)}
  .hero-strip{left:0;top:242px;width:164px;height:27px;
    clip-path:polygon(0 0,100% 0,92% 100%,0 100%);background:var(--orange-grad)}
  .hero-title{left:26px;top:118px;font-weight:800;font-size:38px;line-height:37px;color:var(--white);letter-spacing:.5px}
  .hero-sub{left:26px;top:197px;font-weight:600;font-size:11.5px;line-height:12.5px;color:var(--white)}
  .benefit-panel{left:221px;top:280px;width:203px;height:258px;background:linear-gradient(180deg,#e8e8e8,#d4d4d4)}

  .section-head{font-size:19px;line-height:24px}
  .section-head .light{font-weight:300;display:block}
  .section-head .strong{font-weight:700;color:var(--orange);display:block}
  .task-head{left:26px;top:306px}
  .solution-head{left:249px;top:306px}
  .task-copy{left:26px;top:367px;width:180px;font-size:10.5px;line-height:13.4px}
  .task-copy p{margin-bottom:13px}
  .task-copy .emph{font-weight:700}

  .benefit-list{left:249px;top:368px;list-style:none;font-size:10.5px;line-height:13.4px}
  .benefit-list li{display:flex;gap:7px;margin-bottom:6px}
  .tick{flex:none;width:12px;height:12px;margin-top:1px}

  .footer-strip{left:0;top:529px;width:112px;height:9px;clip-path:polygon(0 0,100% 0,95% 100%,0 100%);background:var(--orange-grad)}
  .front-footer{left:0;top:538px;width:424px;height:60px;background:var(--orange-grad);color:var(--white)}
  .contact-label{left:28px;top:12px;font-weight:600;font-size:11.5px}
  .contact-row{display:flex;gap:16px;font-weight:500;font-size:11px;align-items:center}
  .contact-row span{display:flex;align-items:center;gap:4px}
  .contact-row svg{width:10px;height:10px}
  .front-footer .contact-row{position:absolute;left:27px;top:34px}

  /* ---------- back ---------- */
  .back-top{left:0;top:0;width:424px;height:193px;background:#e4e4e4}
  .tablet-photo{left:156px;top:0;width:268px;height:193px;
    clip-path:polygon(0 0,100% 0,100% 100%,32% 100%);
    background:radial-gradient(circle at 65% 45%,#f4f4f4 0%,#d9dcd9 40%,#9aa59a 80%,#6f7e70 100%)}
  .offer-band{left:0;top:16px;width:259px;height:156px;
    clip-path:polygon(0 0,78% 0,100% 100%,0 100%);background:var(--orange-grad)}
  .offer-title{left:25px;top:40px;font-weight:800;font-size:20px;line-height:25px;color:var(--white)}
  .offer-points{left:25px;top:103px;list-style:none;font-weight:600;font-size:11.5px;line-height:15px;color:var(--white)}
  .offer-points li::before{content:"· "}

  .block-title{width:424px;left:0;text-align:center;font-weight:700;font-size:19px;color:var(--orange)}
  .steps-title{top:205px}
  .steps{left:17px;top:246px;width:387px;height:111px;display:flex}
  .step{flex:1;border-left:1px solid var(--orange);display:flex;flex-direction:column;align-items:center;padding:0 5px;text-align:center;font-size:9px;line-height:11px}
  .step:last-child{border-right:1px solid var(--orange)}
  .step-icon{width:27px;height:27px;border-radius:50%;background:linear-gradient(135deg,var(--orange-light),var(--orange-dark));display:flex;align-items:center;justify-content:center;margin-bottom:10px}
  .step-icon svg{width:15px;height:15px}

  .offer-section{left:0;top:371px;width:424px;height:127px;background:linear-gradient(180deg,#dcdcdc,#d0d0d0)}
  .offer-head{top:384px}
  .service-grid{left:0;top:421px;width:424px;display:grid;grid-template-columns:203px 190px;column-gap:12px;row-gap:6px;font-weight:600;font-size:10.5px;line-height:14px}
  .service{display:flex;align-items:center;gap:6px}
  .service.left{justify-content:flex-end}

  .back-strip{left:310px;top:488px;width:114px;height:10px;clip-path:polygon(0 0,100% 0,100% 100%,6% 100%);background:linear-gradient(90deg,var(--orange-dark),var(--orange-light))}
  .back-footer{left:0;top:498px;width:424px;height:100px;background:var(--orange-grad);color:var(--white)}
  .back-footer-copy{left:28px;top:22px;font-weight:600;font-size:11.5px;line-height:15px;width:370px}
  .back-footer .contact-row{position:absolute;left:27px;top:62px}
</style>
</head>
<body>

<!-- Vorderseite -->
<section class="flyer-page flyer-front">
  <div class="abs front-top"></div>
  <div class="abs brand"><span class="brand-name">TAVOLU</span><span class="brand-dot"></span></div>
  <div class="abs city-photo" role="img" aria-label="Luftbild einer Großstadt bei Nacht mit leuchtenden Netzwerklinien"></div>
  <div class="abs corner-shape-light"></div>
  <div class="abs corner-shape"></div>
  <div class="abs hero-band"></div>
  <div class="abs hero-strip"></div>
  <h1 class="abs hero-title">SMART<br>CITY</h1>
  <p class="abs hero-sub">Grundwasserpegel-Messung<br>per Funk</p>

  <div class="abs benefit-panel"></div>

  <h2 class="abs section-head task-head"><span class="light">Ihre Aufgabe -</span><span class="strong">Ein Problem?</span></h2>
  <div class="abs task-copy">
    <p>Ist die Erfüllung ihrer hoheitlichen Aufgabe der Grundwasserüberwa&shy;chung ungenau und aufwendig?</p>
    <p class="emph">Das muss nicht sein!</p>
    <p>Die regelmäßige Übertragung an das Umweltamt können Sie jetzt auch mit unserer IoT Lösung digitalisieren.</p>
  </div>

  <h2 class="abs section-head solution-head"><span class="light">Unsere Lösung -</span><span class="strong">Ihre Vorteile</span></h2>
  <ul class="abs benefit-list">
    <li><svg class="tick" viewBox="0 0 12 12"><circle cx="6" cy="6" r="5.2" fill="none" stroke="#e0601b" stroke-width="1.2"/><path d="M3.5 6.2l1.8 1.7 3.3-3.6" fill="none" stroke="#e0601b" stroke-width="1.2"/></svg><span>Zuverlässige Übermittlung<br>an das Umweltamt</span></li>
    <li><svg class="tick" viewBox="0 0 12 12"><circle cx="6" cy="6" r="5.2" fill="none" stroke="#e0601b" stroke-width="1.2"/><path d="M3.5 6.2l1.8 1.7 3.3-3.6" fill="none" stroke="#e0601b" stroke-width="1.2"/></svg><span>Echtzeit Überwachung<br>Keine manuelle Messung</span></li>
    <li><svg class="tick" viewBox="0 0 12 12"><circle cx="6" cy="6" r="5.2" fill="none" stroke="#e0601b" stroke-width="1.2"/><path d="M3.5 6.2l1.8 1.7 3.3-3.6" fill="none" stroke="#e0601b" stroke-width="1.2"/></svg><span>Kosten sparen</span></li>
    <li><svg class="tick" viewBox="0 0 12 12"><circle cx="6" cy="6" r="5.2" fill="none" stroke="#e0601b" stroke-width="1.2"/><path d="M3.5 6.2l1.8 1.7 3.3-3.6" fill="none" stroke="#e0601b" stroke-width="1.2"/></svg><span>Datenanalyse<br>&amp; Visualisierung</span></li>
  </ul>

  <div class="abs footer-strip"></div>
  <footer class="abs front-footer">
    <p class="abs contact-label">Kontakt:</p>
    <div class="contact-row">
      <span><svg viewBox="0 0 10 10"><path d="M2 1l2 2-1 1.2c.6 1.2 1.6 2.2 2.8 2.8L7 6l2 2-1.3 1.3C4.5 9 1 5.5.7 2.3z" fill="none" stroke="#fff" stroke-width=".8"/></svg>+49(0)1523448710</span>
      <span><svg viewBox="0 0 10 10"><rect x=".6" y="2" width="8.8" height="6" fill="none" stroke="#fff" stroke-width=".8"/><path d="M.6 2L5 5.5 9.4 2" fill="none" stroke="#fff" stroke-width=".8"/></svg>iot@tavolu.me</span>
      <span><svg viewBox="0 0 10 10"><circle cx="5" cy="5" r="4.3" fill="none" stroke="#fff" stroke-width=".8"/><ellipse cx="5" cy="5" rx="1.8" ry="4.3" fill="none" stroke="#fff" stroke-width=".7"/><path d="M.7 5h8.6" stroke="#fff" stroke-width=".7"/></svg>www.tavolu.me</span>
    </div>
  </footer>
</section>

<!-- Rückseite -->
<section class="flyer-page flyer-back">
  <div class="abs back-top"></div>
  <div class="abs tablet-photo" role="img" aria-label="Hände bedienen ein Tablet mit Messwert-Diagramm und Lagekarte"></div>
  <div class="abs offer-band"></div>
  <h2 class="abs offer-title">Pilotprojekt<br>ab 4.999€</h2>
  <ul class="abs offer-points">
    <li>Abdeckung von 3 Messstellen</li>
    <li>Datenvisualisierung</li>
    <li>3 Monate Betrieb inklusive</li>
  </ul>

  <h2 class="abs block-title steps-title">Die Umsetzung</h2>
  <div class="abs steps">
    <div class="step">
      <div class="step-icon"><svg viewBox="0 0 16 16"><circle cx="4" cy="8" r="2" fill="none" stroke="#fff" stroke-width="1.1"/><circle cx="12" cy="3.5" r="2" fill="none" stroke="#fff" stroke-width="1.1"/><circle cx="12" cy="12.5" r="2" fill="none" stroke="#fff" stroke-width="1.1"/><path d="M5.8 7l4.4-2.5M5.8 9l4.4 2.5" stroke="#fff" stroke-width="1.1"/></svg></div>
      <p>Grundwasserspiegel-Messstellen werden mit IoT-Sensoren ausgestattet, die den Wasserspiegel über den hydrostatischen Druck messen.</p>
    </div>
    <div class="step">
      <div class="step-icon"><svg viewBox="0 0 16 16"><path d="M8 2.5a4 4 0 0 0-2.3 7.3V11.5h4.6V9.8A4 4 0 0 0 8 2.5z" fill="none" stroke="#fff" stroke-width="1.1"/><path d="M6.3 13.3h3.4" stroke="#fff" stroke-width="1.1"/></svg></div>
      <p>Die gemessenen Werte werden über Funk übermit&shy;telt, sodass eine Begehung, Öffnung der Messstelle und anschließende manuelle Messung nicht mehr erfolgen muss.</p>
    </div>
    <div class="step">
      <div class="step-icon"><svg viewBox="0 0 16 16"><circle cx="8" cy="8" r="2.2" fill="none" stroke="#fff" stroke-width="1.1"/><circle cx="8" cy="8" r="4.8" fill="none" stroke="#fff" stroke-width="1.1" stroke-dasharray="2.2 1.6"/></svg></div>
      <p>Die Messwerte können in Echtzeit jederzeit online aufgerufen werden. Wahlweise können die Daten in ihre bestehende Smart City Plattform eingebunden werden.</p>
    </div>
  </div>

  <div class="abs offer-section"></div>
  <h2 class="abs block-title offer-head">Unser Angebot</h2>
  <div class="abs service-grid">
    <div class="service left">Konzeption<svg class="tick" viewBox="0 0 12 12"><circle cx="6" cy="6" r="5.2" fill="none" stroke="#e0601b" stroke-width="1.2"/><path d="M3.5 6.2l1.8 1.7 3.3-3.6" fill="none" stroke="#e0601b" stroke-width="1.2"/></svg></div>
    <div class="service"><svg class="tick" viewBox="0 0 12 12"><circle cx="6" cy="6" r="5.2" fill="none" stroke="#e0601b" stroke-width="1.2"/><path d="M3.5 6.2l1.8 1.7 3.3-3.6" fill="none" stroke="#e0601b" stroke-width="1.2"/></svg>Funktionalitätstest</div>
    <div class="service left">Hardwareauswahl<svg class="tick" viewBox="0 0 12 12"><circle cx="6" cy="6" r="5.2" fill="none" stroke="#e0601b" stroke-width="1.2"/><path d="M3.5 6.2l1.8 1.7 3.3-3.6" fill="none" stroke="#e0601b" stroke-width="1.2"/></svg></div>
    <div class="service"><svg class="tick" viewBox="0 0 12 12"><circle cx="6" cy="6" r="5.2" fill="none" stroke="#e0601b" stroke-width="1.2"/><path d="M3.5 6.2l1.8 1.7 3.3-3.6" fill="none" stroke="#e0601b" stroke-width="1.2"/></svg>Visualisierung</div>
    <div class="service left">Konfiguration und Einrichtung<svg class="tick" viewBox="0 0 12 12"><circle cx="6" cy="6" r="5.2" fill="none" stroke="#e0601b" stroke-width="1.2"/><path d="M3.5 6.2l1.8 1.7 3.3-3.6" fill="none" stroke="#e0601b" stroke-width="1.2"/></svg></div>
    <div class="service"><svg class="tick" viewBox="0 0 12 12"><circle cx="6" cy="6" r="5.2" fill="none" stroke="#e0601b" stroke-width="1.2"/><path d="M3.5 6.2l1.8 1.7 3.3-3.6" fill="none" stroke="#e0601b" stroke-width="1.2"/></svg>Betrieb</div>
  </div>

  <div class="abs back-strip"></div>
  <footer class="abs back-footer">
    <p class="abs back-footer-copy">Für Ihr Pilotprojekt und andere IoT Anwendungen im Bereich Smart City erreichen Sie uns hier:</p>
    <div class="contact-row">
      <span><svg viewBox="0 0 10 10"><path d="M2 1l2 2-1 1.2c.6 1.2 1.6 2.2 2.8 2.8L7 6l2 2-1.3 1.3C4.5 9 1 5.5.7 2.3z" fill="none" stroke="#fff" stroke-width=".8"/></svg>+49(0)1523448710</span>
      <span><svg viewBox="0 0 10 10"><rect x=".6" y="2" width="8.8" height="6" fill="none" stroke="#fff" stroke-width=".8"/><path d="M.6 2L5 5.5 9.4 2" fill="none" stroke="#fff" stroke-width=".8"/></svg>iot@tavolu.me</span>
      <span><svg viewBox="0 0 10 10"><circle cx="5" cy="5" r="4.3" fill="none" stroke="#fff" stroke-width=".8"/><ellipse cx="5" cy="5" rx="1.8" ry="4.3" fill="none" stroke="#fff" stroke-width=".7"/><path d="M.7 5h8.6" stroke="#fff" stroke-width=".7"/></svg>www.tavolu.me</span>
    </div>
  </footer>
</section>

</body>
</html>
```